Website Re-Design and Refresh

We are looking for a redesign of www.brightlark-example.com the deliverable is a graphic which will be used as a template for the main site.
The Logo will remain the same
The Video currently shown must be included in your submission
Search Element must be included, this should be better visible than it is currently
All navigation current on the left is to be moved to the right.
Top left column should be a “Quick Quotation” element. It should stand out and draw the eye as that is the conversion that we aim for on our site. This is the purpose of the site to attract these.
Add Testimonials navigation that users can click upon.
Below this element on the right “Recent Posts” should become Latest News”
We want users to see how much press coverage the site has had, the following UK’s news logos should be used Morrow Ledger, Evening Quill, NVR and The Wayfarer.
Please use the current text from our site but make some main features which we want to draw attention to. 5 points and use fake text, using a bullet point, icon, graphic or colour to make it stick out the most.
Large Guarantee, shown through a Seal graphic. An example of this type of style is attached.
Updates

Please note that as per the brief we want to havenews/contact forms down the left hand side of the page. This is to comply with “F”shapeeye pattern which shows that users look mostly on the left of webpages.

Please make the quick quotes more distinctive and use of thefields suggested in the brief.

As you appear to like using vivid colours, please see thefollowing examples we like of vivid colours.

 

http://media.tundrasquare.example/cpw-sales/static/images/common/global_nav/nnp_03.png

http://media.tundrasquare.example/cpw-sales/static/sections/homepage/2012_04/images/ban_big_promises.png

http://media.tundrasquare.example/cpw-sales/static/images/landing_pages/mobile_phones/April_2012/mp_hero2_v3.jpg

http://media.tundrasquare.example/cpw-sales/static/sections/upgrades/images/sidebanner_payg_upgrades.gif

Pleaseamend your designs so that they adhere to the following:

 

Thereis a quick quotation form, as per brief, next to the video positionedon the left, the video on the right so they are the first items the userssee. 

 

The"seal" guarantee should be top right and 

Newsand Testimonials should be on the right hand side

 

Inthe main content text area please use latin ipsom lorem text and put 5 bulletpoints in large writing and latin below. Such as:

 

Lorem Ipsum 

Lorem Ipsum 

Lorem Ipsum 

Lorem Ipsum 

Lorem Ipsum 

 

Lorem Ipsum is simply dummy text ofthe printing and typesetting industry. Lorem Ipsum has been the industry'sstandard dummy text ever since the 1500s, when an unknown printer took a galleyof type and scrambled it to make a type specimen book. It has survived not onlyfive centuries, but also the leap into electronic typesetting, remainingessentially unchanged. It was popularised in the 1960s with the release ofLetraset sheets containing Lorem Ipsum passages, and more recently with desktoppublishing software like Orvel SheetCraft including versions of Lorem Ipsum.

The following design is a good indication of style and the use of bright colors. Although the positioning of some elements is not as per the brief. 

Please see best deigns so far:

Target Market(s)

Business To Business

Industry/Entity Type

News

Requirements
Must have
• The Logo will remain the same
Top right should be a “Quick Quotation” element. It should stand out and draw the eye as that is the conversion that we aim for on our site. This is the purpose of the site to attract these.

```html
<!DOCTYPE html>
<html lang="en">
<head>
<meta charset="utf-8">
<title>brightlark – Reputation Management</title>
<link rel="stylesheet" href="https://fonts.googleapis.com/css2?family=Arimo:wght@400;700&family=Open+Sans:wght@400;600;700&display=swap">
<style>
:root{
  --green-dark:#1f5a06;
  --green-bar-top:#5f8a1f;
  --green-bar-bot:#3b640f;
  --logo-green:#5aa51e;
  --page-bg:#ebebeb;
  --panel-bg:#e6e6e6;
  --content-bg:#eef3e1;
  --footer-bg:#272727;
  --text:#333333;
  --muted:#8a8a8a;
  --white:#ffffff;
  --rule:#d4d4d4;
}
*{box-sizing:border-box;margin:0;padding:0}
html,body{width:878px;height:1200px;overflow:hidden}
body{position:relative;background:var(--page-bg);font-family:"Arimo",Arial,sans-serif;color:var(--text);font-size:11px}
.abs{position:absolute}

/* header */
.site-header{left:0;top:0;width:878px;height:130px;background:var(--white);border-top:2px solid #ddd}
.brand{left:72px;top:46px;font-family:"Open Sans",Arial,sans-serif;font-weight:700;font-size:34px;color:var(--logo-green);letter-spacing:-1px;display:flex;align-items:center;gap:8px}
.brand-square{width:22px;height:22px;background:var(--logo-green)}
.phone{left:550px;top:18px;display:flex;align-items:center;gap:8px;font-family:"Open Sans",Arial,sans-serif;font-size:16px;color:#333}
.phone-rule{left:530px;top:58px;width:280px;height:1px;background:linear-gradient(90deg,transparent,#ccc,transparent)}
.search{left:560px;top:79px;display:flex}
.search-field{width:207px;height:25px;border:1px solid #999;border-radius:3px 0 0 3px;background:linear-gradient(#f1f1f1,#e2e2e2);font-size:10px;color:#999;padding:6px 12px}
.search-btn{width:27px;height:25px;background:#222;display:flex;align-items:center;justify-content:center}

/* nav */
.main-nav{left:0;top:130px;width:878px;height:40px;background:var(--green-dark)}
.main-nav a{position:absolute;top:10px;color:var(--white);text-decoration:none;font-size:11px;line-height:20px;white-space:nowrap}
.main-nav a+a::before{content:"";position:absolute;left:-12px;top:0;width:1px;height:20px;background:#3d7a1f}

/* panels */
.panel{background:var(--panel-bg);border:1px solid #d8d8d8;border-radius:3px}
.panel-head{height:32px;background:linear-gradient(var(--green-bar-top),var(--green-bar-bot));border:1px solid #2f520a;border-radius:3px 3px 0 0;color:var(--white);font-family:"Open Sans",Arial,sans-serif;font-size:14px;display:flex;align-items:center;gap:9px;padding-left:10px;margin:-1px -1px 0}
.quote{left:70px;top:183px;width:173px;height:192px}
.quote-field{margin:13px 0 0 14px;width:133px;height:25px;border:1px solid #888;border-radius:4px;background:#ececec;box-shadow:inset 0 1px 2px #bbb;font-size:10px;color:#888;padding:7px 7px}
.pill{display:inline-block;border:1px solid #bbb;border-radius:10px;background:linear-gradient(#f4f4f4,#d9d9d9);font-size:11px;color:#111;padding:2px 12px}
.quote .pill{margin:14px 0 0 81px}
.news{left:70px;top:390px;width:173px;height:350px}
.news ul{list-style:none}
.news li{font-size:10.5px;line-height:15.5px;padding:6px 8px 6px 16px;border-bottom:1px solid var(--rule);position:relative;height:47px}
.news li::before{content:"›";position:absolute;left:6px;top:4px;font-size:14px;color:#444}
.news .pill{margin:8px 0 0 94px;font-size:10.5px}
.recent{left:70px;top:761px;width:173px;height:243px}
.recent-item{padding:8px 10px 0 11px;font-size:10.5px;line-height:15.5px}
.recent-date{color:var(--muted);font-size:9.5px}

/* main */
.video{left:259px;top:183px;width:547px;height:298px;border:1px solid #4d7b25;background:var(--white);overflow:hidden}
.video-frame{width:100%;height:279px;background:linear-gradient(180deg,#eef1fb 0%,#f6f7ee 40%,#eef2fa 55%,#f7f3ee 75%,#fdfdfd 100%)}
.video-bar{width:100%;height:18px;background:#111}
.about{left:259px;top:497px;width:547px;height:507px;background:var(--content-bg);border-color:#dce3c8}
.about-intro{padding:16px 14px 0;font-size:10.5px;line-height:15.5px}
.about ul{padding:16px 0 0 27px;font-weight:700;font-size:10.5px;line-height:21px}
.about-rule{margin:11px 18px 0 10px;height:1px;background:#cdd5b8}
.about-media{display:flex;padding:13px 0 0 14px;gap:15px}
.photo{width:289px;height:134px;border:2px solid #222;padding:9px 8px}
.photo-fill{width:100%;height:100%;background:linear-gradient(90deg,#e9ebe8 0%,#9a9c98 30%,#3a3a3a 50%,#b9bab6 70%,#2b2b2b 90%,#e5e6e2 100%)}
.about-side{width:215px;font-size:10.5px;line-height:15.5px;margin-top:2px}
.about-body{padding:13px 14px 0 16px;font-size:10.5px;line-height:15.5px}
.about .pill{margin:13px 0 0 17px}

/* footer */
.site-footer{left:0;top:1032px;width:878px;height:168px;background:var(--footer-bg)}
.info-title{left:70px;top:1062px;color:var(--white);font-size:14px;font-weight:400}
.info-links{left:71px;top:1089px;list-style:none;color:#aaa;font-size:10.5px;line-height:18px}
.press{top:1083px;height:32px;background:var(--white);display:flex;align-items:center;justify-content:center;font-family:"Open Sans",Arial,sans-serif;font-weight:700;font-size:10.5px;color:#111;white-space:nowrap}
.seal{left:629px;top:1046px;width:166px;height:97px;border:2px solid #111;background:linear-gradient(135deg,#3a2018 0%,#e9e0c6 30%,#e2d7b7 60%,#c8561e 80%,#5a2a16 100%)}
.footer-rule{left:70px;top:1156px;width:736px;height:1px;background:#444}
.copyright{left:71px;top:1162px;color:#ddd;font-size:9.5px}
.connect{left:630px;top:1163px;display:flex;align-items:center;gap:7px;color:var(--white);font-size:14px}
.social{display:flex;align-items:center;gap:3px;font-size:9px;color:#cfe3f5}
.social i{display:block;width:20px;height:20px;background:#4a8fd0;border-radius:3px}
</style>
</head>
<body>

<header class="site-header abs">
  <div class="brand abs"><span class="brand-square"></span>brightlark</div>
  <div class="phone abs">
    <svg width="14" height="22" viewBox="0 0 14 22"><path d="M4 1 L7 1 L8 6 L5.5 7.5 Q5 11 8 15 L10.5 14 L13 18 L10 21 Q2 19 1 9 Q1 3 4 1Z" fill="#222"/></svg>
    0800 555 0142
  </div>
  <div class="phone-rule abs"></div>
  <form class="search abs">
    <div class="search-field">Search</div>
    <div class="search-btn"><svg width="12" height="12" viewBox="0 0 12 12"><circle cx="5" cy="5" r="3.5" stroke="#d6b52a" stroke-width="2" fill="none"/><path d="M7.5 7.5 L11 11" stroke="#d6b52a" stroke-width="2"/></svg></div>
  </form>
</header>

<nav class="main-nav abs">
  <a href="#" style="left:70px">REPUTATION MANAGEMENT</a>
  <a href="#" style="left:238px">ONLINE REPUTATION MANAGEMENT – ORM</a>
  <a href="#" style="left:489px">BRAND PROTECTION</a>
  <a href="#" style="left:622px">PRICES</a>
  <a href="#" style="left:683px">TESTIMONIAL</a>
</nav>

<section class="quote panel abs">
  <div class="panel-head">
    <svg width="16" height="14" viewBox="0 0 16 14"><path d="M1 4h4V1h5v3h4v4h-3v5H6V8H1z" fill="#fff"/></svg>
    Quick Quotation
  </div>
  <div class="quote-field">Name</div>
  <div class="quote-field">Email</div>
  <div class="quote-field">Phone</div>
  <span class="pill">SUBMIT</span>
</section>

<section class="news panel abs">
  <div class="panel-head">
    <svg width="18" height="14" viewBox="0 0 18 14"><path d="M9 7 Q3 0 1 4 Q3 9 9 7 Q15 9 17 4 Q15 0 9 7 L5 13 M9 7 L13 13" stroke="#fff" stroke-width="1.3" fill="none"/></svg>
    Latest News
  </div>
  <ul>
    <li>Lorem Ipsum montori illi ko naop ta lo&nbsp; kop</li>
    <li>Monatre ilopuo toploiu jkop tapoiy nasile</li>
    <li>Lorem Ipsum montori illi ko naop ta lo&nbsp; kop</li>
    <li>Monatre ilopuo toploiu jkop tapoiy nasile</li>
    <li>Lorem Ipsum montori illi ko naop ta lo&nbsp; kop</li>
    <li>Monatre ilopuo toploiu jkop tapoiy nasile</li>
  </ul>
  <span class="pill">read more</span>
</section>

<section class="recent panel abs">
  <div class="panel-head">
    <svg width="14" height="16" viewBox="0 0 14 16"><path d="M3 9V3M6 8V1M9 8V2M12 9V4M3 9 Q2 15 7 15 Q12 15 12 9" stroke="#fff" stroke-width="1.5" fill="none" stroke-linecap="round"/></svg>
    Recent Post
  </div>
  <div class="recent-item">Lorem Ipsum is simply dummy text of the printing and type-setting industry.<div class="recent-date">26th April, 2012</div></div>
  <div class="recent-item">Lorem Ipsum is simply dummy text of theTolpop.<div class="recent-date">26th April, 2012</div></div>
  <div class="recent-item">Lorem Ipsum is simply dummy text of theTolpop.<div class="recent-date">26th April, 2012</div></div>
</section>

<div class="video abs">
  <div class="video-frame" role="img" aria-label="Company video: a search results page listing negative national and international news about a brand"></div>
  <div class="video-bar"></div>
</div>

<section class="about panel abs">
  <div class="panel-head">
    <svg width="20" height="18" viewBox="0 0 20 18"><circle cx="6" cy="3" r="2" fill="#fff"/><circle cx="14" cy="3" r="2" fill="#fff"/><path d="M4 6h4l1 6H7v6H5v-6H3zM12 6h4l1 6h-2v6h-2v-6h-2z" fill="#fff"/></svg>
    About Us
  </div>
  <p class="about-intro">Lorem Ipsum is simply dummy text of the printing and typesetting industry. Lorem Ipsum has been the industry's standard dummy text ever since the 1500s, when an unknown printer took a galley of type and scrambled it to make a type specimen book.</p>
  <ul>
    <li>Lorem Ipsum is simply dummy text of the printing</li>
    <li>It has survived not only five centuries, but also the leap into electronic typesetting,</li>
    <li>We offer all logistics services for the domestic network.</li>
    <li>Lorem Ipsum passages, and more recently with desktop publishing software like Orvel SheetCraft.</li>
    <li>It is a long established fact that a reader will be distracted by the readable.</li>
  </ul>
  <div class="about-rule"></div>
  <div class="about-media">
    <div class="photo"><div class="photo-fill" role="img" aria-label="Photo of three business people in dark suits working together at a laptop"></div></div>
    <p class="about-side">Lorem Ipsum is simply dummy text of the printing and typesetting industry. Lorem Ipsum has been the industry's standard dummy text ever since the 1500s,<br>Lorem Ipsum is simply dummy text of the printing and typesetting industry. Lorem Ipsum has been the industry's standard dummy text ever since the 1500s,</p>
  </div>
  <p class="about-body">Lorem Ipsum is simply dummy text of the printing and typesetting industry. Lorem Ipsum has been the industry's standard dummy text ever since the 1500s,<br>Lorem Ipsum is simply dummy text of the printing and typesetting industry. Lorem Ipsum has been the industry's standard dummy text ever since the 1500s,</p>
  <span class="pill">View more</span>
</section>

<footer class="site-footer abs"></footer>
<h3 class="info-title abs">Information</h3>
<ul class="info-links abs"><li>About us</li><li>Customer Service</li><li>Site Map</li></ul>
<div class="press abs" style="left:201px;width:86px">Morrow Ledger</div>
<div class="press abs" style="left:296px;width:84px">Evening Quill</div>
<div class="press abs" style="left:388px;width:85px">NVR</div>
<div class="press abs" style="left:482px;width:113px">The Wayfarer</div>
<div class="seal abs" role="img" aria-label="Framed money back guarantee certificate with a cartoon mascot standing beside it"></div>
<div class="footer-rule abs"></div>
<p class="copyright abs">Copyright@2012.All right reserved</p>
<div class="connect abs">Connect with us
  <span class="social"><i></i>Chatterly</span>
  <span class="social"><i></i>Flitbird</span>
</div>

</body>
</html>
```